New Business Card Design Project

I need a meaningful new business card. Therefore, the website should convey growth, joy, uniqueness, workout and a bit of luxury.
Color scheme should be petrol, gold and matching colors.

```html
<!DOCTYPE html>
<html lang="en">
<head>
<meta charset="utf-8">
<title>Corewell Studio – Business Card</title>
<link href="https://fonts.googleapis.com/css2?family=Cinzel:wght@500&family=Poppins:wght@400;500&display=swap" rel="stylesheet">
<style>
  :root {
    --petrol: #15a89c;
    --gold: #c9a24a;
    --ink: #1b1b1c;
    --paper: #ffffff;
    --text-grey: #3c3c3e;
    --stage: #ecebe8;
  }
  * { box-sizing: border-box; margin: 0; padding: 0; }
  html, body { width: 1200px; height: 900px; overflow: hidden; background: var(--stage); }
  body { position: relative; font-family: "Poppins", sans-serif; }

  .card {
    position: absolute;
    left: 250px;
    width: 700px;
    height: 400px;
    overflow: hidden;
    box-shadow: 0 6px 18px rgba(0,0,0,0.18);
  }
  .card--back { top: 40px; background: var(--ink); }
  .card--front { top: 470px; background: var(--paper); }

  .card__frame {
    position: absolute;
    inset: 18px;
    border: 1px solid var(--gold);
    opacity: 0.7;
  }

  .brand {
    position: absolute;
    display: flex;
    align-items: center;
    gap: 12px;
    color: var(--petrol);
    font-family: "Poppins", sans-serif;
    font-weight: 500;
    white-space: nowrap;
  }
  .brand__dot {
    border-radius: 50%;
    background: var(--gold);
    flex: none;
  }
  .card--back .brand { left: 50%; top: 50%; transform: translate(-50%, -50%); font-size: 40px; }
  .card--back .brand__dot { width: 26px; height: 26px; }
  .card--front .brand { right: 44px; top: 70px; font-size: 26px; }
  .card--front .brand__dot { width: 18px; height: 18px; }

  .card__wave { position: absolute; inset: 0; width: 700px; height: 400px; }

  .holder { position: absolute; left: 56px; top: 88px; }
  .holder__name {
    font-family: "Cinzel", serif;
    font-weight: 500;
    color: var(--petrol);
    font-size: 25px;
    letter-spacing: 2px;
    line-height: 1.1;
  }
  .holder__rule {
    width: 60px;
    height: 2px;
    background: var(--gold);
    margin: 6px 0 4px;
  }
  .holder__role { color: var(--text-grey); font-size: 19px; line-height: 1.3; }

  .contact { position: absolute; left: 70px; top: 182px; list-style: none; color: var(--text-grey); font-size: 17px; }
  .contact__item { display: flex; align-items: center; gap: 12px; line-height: 1.5; }
  .contact__icon { width: 22px; height: 22px; flex: none; fill: var(--petrol); }
  .contact__address { margin-top: 10px; line-height: 1.35; }

  .website {
    position: absolute;
    right: 40px;
    bottom: 56px;
    color: var(--gold);
    font-size: 17px;
    letter-spacing: 0.3px;
  }
</style>
</head>
<body>

  <section class="card card--back" aria-label="Card back">
    <div class="card__frame"></div>
    <div class="brand"><span class="brand__dot"></span>Corewell Studio</div>
  </section>

  <section class="card card--front" aria-label="Card front">
    <svg class="card__wave" viewBox="0 0 700 400" aria-hidden="true">
      <path d="M0,318 C200,325 350,275 470,190 C360,285 210,340 0,342 Z" fill="#15a89c"/>
      <path d="M0,350 C220,350 360,300 480,215 C560,170 640,150 700,142 L700,400 L0,400 Z" fill="#1b1b1c"/>
      <path d="M0,350 C220,350 360,300 480,215 C560,170 640,150 700,142" fill="none" stroke="#c9a24a" stroke-width="2"/>
    </svg>

    <div class="brand"><span class="brand__dot"></span>Corewell Studio</div>

    <div class="holder">
      <p class="holder__name">DANIEL MARSH</p>
      <div class="holder__rule"></div>
      <p class="holder__role">Managing Director</p>
    </div>

    <ul class="contact">
      <li class="contact__item">
        <svg class="contact__icon" viewBox="0 0 24 24"><path d="M6.6 10.8a15.2 15.2 0 0 0 6.6 6.6l2.2-2.2a1 1 0 0 1 1-.25 11.4 11.4 0 0 0 3.6.57 1 1 0 0 1 1 1V20a1 1 0 0 1-1 1A17 17 0 0 1 3 4a1 1 0 0 1 1-1h3.5a1 1 0 0 1 1 1c0 1.25.2 2.45.57 3.570a1 1 0 0 1-.25 1z"/></svg>
        <span>041-555 203 118</span>
      </li>
      <li class="contact__item">
        <svg class="contact__icon" viewBox="0 0 24 24"><path d="M2 5h20v14H2z M3.5 6.5 12 13l8.5-6.5" fill="none" stroke="#15a89c" stroke-width="2"/></svg>
        <span>hello@corewellstudio.com</span>
      </li>
      <li class="contact__address">18 Linden Row<br>Easton, 40721</li>
    </ul>

    <p class="website">www.corewellstudio.com</p>
  </section>

</body>
</html>
```